Business Card design for a skin clinic

i would like a business card design for our skin clinic.
our logo colors are Blue and Grey and Bule /white.
we are searching for a minimalistic design yet very elegant,dynamic and professional which can reflect a professional medical skin care clinic( not a beauty salon).
THE DESGIN IS NOT FOR A PERSON IT WILL BE USED IN THE CLINIC FOR CLIENTS SO THERE SHOULD BE NO NAME OF A PERSON ONLY THE CLINIC NAME AND THE CONTACT INFO

Target Market(s)
young and old womens
Industry/Entity Type
Business
Contact Information for Business Card
we have 2 address and both should be on the card.
address A: Lindenhoflaan 214B, 3041KP Rotterdam, Tel 010 483 21 95
address B: Zonnewijzerstraat 238, 1062RT Amsterdam Tel 020 571 3829
website www.huidpuntzorg.nu, email info@huidpuntzorg.nu
Look and feel
Each slider illustrates characteristics of the customer's brand and the style your logo design should communicate.

```html
<!DOCTYPE html>
<html lang="nl">
<head>
<meta charset="utf-8">
<title>Huidpuntzorg – visitekaartjes</title>
<link href="https://fonts.googleapis.com/css2?family=Quicksand:wght@500&family=Open+Sans:wght@400&display=swap" rel="stylesheet">
<style>
  :root {
    --page-bg: #eef0f2;
    --card-white: #ffffff;
    --brand-blue: #3b86d0;
    --band-blue: #3d8ad4;
    --brand-grey: #6d6f73;
    --navy: #141b26;
    --photo-light-a: #8ec9dc;
    --photo-light-b: #c6e8f2;
    --photo-dark-a: #2a4a55;
    --photo-dark-b: #7fb3c4;
    --text-white: #ffffff;
  }
  * { margin: 0; padding: 0; box-sizing: border-box; }
  html, body { width: 960px; height: 1200px; overflow: hidden; background: var(--page-bg); }
  .sheet {
    width: 960px; height: 1200px;
    display: flex; flex-direction: column; align-items: center; justify-content: center; gap: 70px;
  }
  .card {
    position: relative; width: 760px; height: 434px; overflow: hidden;
    box-shadow: 0 6px 24px rgba(0,0,0,0.12);
  }
  .card--front { background: var(--card-white); }
  .card--back { background: var(--navy); }

  .brand { position: absolute; left: 0; right: 0; text-align: center; }
  .brand__name {
    font-family: "Quicksand", sans-serif; font-weight: 500;
    font-size: 52px; letter-spacing: 4px; color: var(--brand-blue);
    display: inline-flex; align-items: center; gap: 16px;
  }
  .brand__dot { width: 18px; height: 18px; border-radius: 50%; background: var(--brand-blue); }
  .brand__tagline {
    font-family: "Quicksand", sans-serif; font-weight: 500;
    font-size: 20px; letter-spacing: 3px; margin-top: 6px;
  }
  .card--front .brand { top: 120px; }
  .card--front .brand__tagline { color: var(--brand-grey); }
  .card--back .brand { top: 150px; }
  .card--back .brand__tagline { color: var(--text-white); }

  .band { position: absolute; left: 0; bottom: 0; width: 760px; height: 150px; }
  .band svg { position: absolute; inset: 0; }
  .contacts {
    position: absolute; left: 0; right: 0; bottom: 0; height: 130px;
    display: flex; align-items: center;
    font-family: "Open Sans", sans-serif; font-size: 15px; line-height: 1.45; color: var(--text-white);
  }
  .contact { flex: 1; padding: 0 36px; }
  .contact--center { text-align: center; border-left: 1px solid rgba(255,255,255,0.6); border-right: 1px solid rgba(255,255,255,0.6); }
  .contact--right { text-align: right; }
  .contact__phone { display: inline-flex; align-items: center; gap: 6px; }
  .icon-phone { width: 14px; height: 14px; }

  .photo { position: absolute; }
  .photo--top {
    left: 34px; top: 30px; width: 600px; height: 78px;
    background: linear-gradient(90deg, var(--photo-light-a), var(--photo-light-b) 60%, var(--photo-light-a));
  }
  .photo--bottom {
    left: 120px; top: 300px; width: 610px; height: 100px;
    background: linear-gradient(90deg, var(--photo-dark-a), var(--photo-dark-b) 55%, var(--photo-dark-a));
  }
</style>
</head>
<body>
<main class="sheet">
  <section class="card card--front" aria-label="Voorzijde visitekaartje">
    <div class="brand">
      <div class="brand__name"><span class="brand__dot"></span>HUIDPUNTZORG</div>
      <div class="brand__tagline">next generation skin care</div>
    </div>
    <div class="band">
      <svg viewBox="0 0 760 150" width="760" height="150" aria-hidden="true">
        <path d="M0 20 H150 L162 8 L174 20 H460 L472 8 L484 20 H760 V150 H0 Z" fill="var(--band-blue)"/>
      </svg>
      <div class="contacts">
        <div class="contact contact--left">
          Lindenhoflaan 214B<br>3041KP Rotterdam<br>
          <span class="contact__phone">
            <svg class="icon-phone" viewBox="0 0 14 14"><circle cx="7" cy="7" r="7" fill="#fff"/><path d="M4 5.5 Q7 3.5 10 5.5 L9 7 H5 Z M4.5 8 H9.5 V10 H4.5 Z" fill="var(--band-blue)"/></svg>
            010 483 21 95
          </span>
        </div>
        <div class="contact contact--center">
          info@huidpuntzorg.nu<br>www.huidpuntzorg.nu
        </div>
        <div class="contact contact--right">
          Zonnewijzerstraat 238<br>1062RT Amsterdam<br>
          <span class="contact__phone">
            020 571 3829
            <svg class="icon-phone" viewBox="0 0 14 14"><circle cx="7" cy="7" r="7" fill="#fff"/><path d="M4 5.5 Q7 3.5 10 5.5 L9 7 H5 Z M4.5 8 H9.5 V10 H4.5 Z" fill="var(--band-blue)"/></svg>
          </span>
        </div>
      </div>
    </div>
  </section>

  <section class="card card--back" aria-label="Achterzijde visitekaartje">
    <div class="photo photo--top" role="img" aria-label="Lichtblauwe foto met zachte bokeh-lichtjes"></div>
    <div class="photo photo--bottom" role="img" aria-label="Donkere blauwgroene foto van water met lichtreflecties"></div>
    <div class="brand">
      <div class="brand__name"><span class="brand__dot"></span>HUIDPUNTZORG</div>
      <div class="brand__tagline">next generation skin care</div>
    </div>
  </section>
</main>
</body>
</html>
```